TRENDY & MODERN BUSINESS CARD DESIGN for Media Company *

I need a minimalistic - clean - modern and professional business card layout and design for MEDIA & PHOTOGRAPHY STUDIO.

We do NOT have a logo, and not really looking for one - but rather excellent typography and design. We would consider the 3 as a focal point.

We do personal and commercial photography.

Target Market(s)

Personal and commercial photography clientele

Contact Information for Business Card

ZUB size - from zub.com / size guidelines are enclosed in the brief

Font styles to use
Sans Serif

Colors
f78f20
eda3c7
cee9f5
0555a3
e667a6
fbf289

Requirements
Must have
• Clean lines - Modern layout
Nice to have
• All blue background as an option - use color palette in brief please.
Should not have
• Old fashion fonts and regular fonts.

```html
<!DOCTYPE html>
<html lang="en">
<head>
<meta charset="utf-8">
<title>Halden Media — Business Card</title>
<link rel="stylesheet" href="https://fonts.googleapis.com/css2?family=Raleway:wght@400;500&display=swap">
<style>
  :root {
    --stage: #1f1f21;
    --brand-blue: #0555a3;
    --brand-blue-light: #1a6cc0;
    --paper: #f7f7f7;
    --ink: #1b1b1b;
    --white: #ffffff;
  }
  * { margin: 0; padding: 0; box-sizing: border-box; }
  html, body {
    width: 1200px; height: 900px; overflow: hidden;
    background: var(--stage);
    font-family: "Raleway", sans-serif;
  }
  .canvas { position: relative; width: 1200px; height: 900px; }

  .card {
    position: absolute;
    width: 560px; height: 320px;
    box-shadow: 0 18px 40px rgba(0,0,0,.55);
  }

  /* Front */
  .card-front {
    left: 70px; top: 70px;
    background: radial-gradient(ellipse at 45% 40%, var(--brand-blue-light), var(--brand-blue) 75%);
    color: var(--white);
    display: flex; flex-direction: column; align-items: center; justify-content: center;
  }
  .front-wordmark {
    font-size: 30px; font-weight: 400; letter-spacing: 12px;
    margin-left: 12px; display: flex; align-items: center; gap: 14px;
  }
  .front-wordmark .dot { width: 14px; height: 14px; border: 2px solid var(--white); border-radius: 50%; }
  .front-cities {
    margin-top: 70px; font-size: 14px; font-weight: 500; letter-spacing: .5px;
    word-spacing: 2px;
  }

  /* Back */
  .card-back {
    left: 570px; top: 470px;
    background: linear-gradient(135deg, #ececec, var(--paper) 45%, #e9e9e9);
    color: var(--ink);
  }
  .person { position: absolute; left: 44px; top: 58px; }
  .person-name { font-size: 26px; font-weight: 400; }
  .person-title { font-size: 15px; color: var(--brand-blue); margin-top: 4px; font-weight: 500; }
  .contact { position: absolute; left: 44px; bottom: 42px; list-style: none; font-size: 14px; font-weight: 500; }
  .contact li { display: flex; align-items: flex-start; gap: 10px; margin-top: 6px; line-height: 1.35; }
  .contact svg { width: 13px; height: 13px; flex: none; margin-top: 3px; fill: var(--brand-blue); }
  .back-wordmark {
    position: absolute; right: 10px; top: 50%;
    transform: translate(50%, -50%) rotate(-90deg) translateY(-60px);
    white-space: nowrap;
    font-size: 22px; letter-spacing: 9px; color: var(--ink);
    display: flex; align-items: center; gap: 12px;
  }
  .back-wordmark .dot { width: 12px; height: 12px; background: var(--brand-blue); border-radius: 50%; }

  /* Brand lockup */
  .lockup {
    position: absolute; left: 70px; top: 780px;
    color: var(--white); font-size: 30px; letter-spacing: 10px;
    display: flex; align-items: center; gap: 16px;
  }
  .lockup .dot { width: 14px; height: 14px; border: 2px solid var(--white); border-radius: 50%; }
</style>
</head>
<body>
<main class="canvas">
  <section class="card card-front">
    <div class="front-wordmark"><span class="dot"></span>HALDEN MEDIA</div>
    <p class="front-cities">Miami • New York • Las Vegas • Cancun • Roma</p>
  </section>

  <section class="card card-back">
    <div class="person">
      <h1 class="person-name">Marisol Ortega</h1>
      <p class="person-title">Founder &amp; Media Director</p>
    </div>
    <ul class="contact">
      <li>
        <svg viewBox="0 0 12 12"><path d="M6 0a4 4 0 0 0-4 4c0 3 4 8 4 8s4-5 4-8a4 4 0 0 0-4-4zm0 5.6A1.6 1.6 0 1 1 6 2.4a1.6 1.6 0 0 1 0 3.2z"/></svg>
        <span>2480 Harbor Avenue<br>9th Floor, Miami, FL 33130</span>
      </li>
      <li>
        <svg viewBox="0 0 12 12"><path d="M1 4c0-1.5 2-2.5 5-2.5S11 2.5 11 4v1H8.5V4h-5v1H1zM2.5 6h7l1 5h-9z"/></svg>
        <span>(305) 555-0148</span>
      </li>
      <li>
        <svg viewBox="0 0 12 12"><path d="M0 2h12v8H0zm1 1v.3l5 3.4 5-3.4V3z"/></svg>
        <span>mo@haldenmedia.com</span>
      </li>
    </ul>
    <div class="back-wordmark"><span class="dot"></span>HALDEN MEDIA</div>
  </section>

  <div class="lockup"><span class="dot"></span>HALDEN MEDIA</div>
</main>
</body>
</html>
```